Wellness Coach/personal trainer Business Card Design Project

We need an eye catching logo design for a wellness coach / personal trainer who specializes in weight loss / body transformation / health coaching. We educate, empower, and support our clients on their weight loss journey. We want the look and feel described below on the business card design.

Target Market(s)

80 % women 20 % men
educated 30 - 50 women
vanity/appearance focused

Industry/Entity Type

Personal Trainer

Font styles to use
Serif

Colors
a54599
f9ed23
ffffff

Requirements
Must have
• name - Dorian Calvaske
phone - (888) 275 9146
web address - www.7PennyMover.example
tagline - Strength Shaped With Grace
Nice to have
• see Look and Feel
Colorful, Playful, Elegant
Should not have
• no cartoons or animation

```html
<!DOCTYPE html>
<html lang="en">
<head>
<meta charset="utf-8">
<title>Lumenform Coaching Business Card</title>
<link rel="stylesheet" href="https://fonts.googleapis.com/css2?family=Lora:ital,wght@0,400;0,700&display=swap">
<style>
  :root {
    --plum: #a54599;
    --sun: #f9ed23;
    --paper: #ffffff;
    --slate: #6b7478;
    --backdrop: #ebe8e3;
  }
  * { margin: 0; padding: 0; box-sizing: border-box; }
  html, body { width: 1200px; height: 870px; overflow: hidden; }
  body {
    background: var(--backdrop);
    display: flex;
    align-items: center;
    justify-content: center;
    gap: 90px;
    font-family: "Lora", serif;
  }
  .card {
    position: relative;
    width: 360px;
    height: 630px;
    background: var(--paper);
    box-shadow: 0 10px 30px rgba(0,0,0,0.12);
    overflow: hidden;
  }
  .card-shape {
    position: absolute;
    inset: 0;
    width: 100%;
    height: 100%;
  }
  .card-content {
    position: absolute;
    inset: 0;
    display: flex;
    flex-direction: column;
    align-items: center;
    text-align: center;
  }
  .brand-mark {
    width: 40px;
    height: 40px;
    border-radius: 50%;
    background: var(--plum);
    flex: none;
  }
  .brand-name {
    font-family: "Lora", serif;
    font-weight: 400;
    font-size: 30px;
    color: var(--plum);
    line-height: 1.1;
  }
  .tagline {
    font-family: "Lora", serif;
    font-size: 14px;
    color: var(--slate);
    letter-spacing: 0.5px;
    margin-top: 6px;
  }

  /* Front */
  .front .card-content { padding-top: 120px; }
  .front .brand-mark { margin-bottom: 30px; }
  .person-name {
    font-weight: 700;
    font-size: 26px;
    color: var(--plum);
    margin-top: 118px;
  }
  .person-role {
    font-size: 16px;
    color: var(--slate);
    margin-top: 2px;
  }
  .contact {
    font-size: 17px;
    color: var(--plum);
    line-height: 1.8;
    margin-top: 58px;
  }

  /* Back */
  .back .card-content {
    padding-top: 250px;
  }
  .brand-lockup {
    display: flex;
    align-items: center;
    gap: 12px;
  }
  .brand-lockup .text { text-align: left; }
  .back .brand-name { font-size: 26px; }
  .back .tagline { font-size: 13px; margin-top: 4px; }
</style>
</head>
<body>
  <article class="card front">
    <svg class="card-shape" viewBox="0 0 360 630" aria-hidden="true">
      <rect width="360" height="630" fill="var(--plum)"/>
      <ellipse cx="175" cy="318" rx="250" ry="345" transform="rotate(-14 175 318)" fill="var(--paper)"/>
    </svg>
    <div class="card-content">
      <div class="brand-mark"></div>
      <div class="brand-name">Lumenform Coaching</div>
      <div class="tagline">Strength Shaped With Grace</div>
      <div class="person-name">Dorian Calvaske</div>
      <div class="person-role">Managing Director</div>
      <div class="contact">
        <div class="phone">(888) 275 9146</div>
        <div class="web">www.7PennyMover.example</div>
      </div>
    </div>
  </article>

  <article class="card back">
    <svg class="card-shape" viewBox="0 0 360 630" aria-hidden="true">
      <rect width="360" height="630" fill="var(--plum)"/>
      <ellipse cx="185" cy="312" rx="250" ry="345" transform="rotate(14 185 312)" fill="var(--paper)"/>
    </svg>
    <div class="card-content">
      <div class="brand-lockup">
        <div class="brand-mark"></div>
        <div class="text">
          <div class="brand-name">Lumenform Coaching</div>
          <div class="tagline">Strength Shaped With Grace</div>
        </div>
      </div>
    </div>
  </article>
</body>
</html>
```